Graphic Design Project

I am looking for a designer to create three simple kitchen tea towel designs using the following text (insert images where appropriate):

'Everything I am, I owe to spaghetti' - Marta Velucci (prefer red)

'Coogee, Bronte, Clovelly, Tamarama, Bondi' (These are names of Sydney beaches. Bondi is the most famous.)

'Desperate Housewife'

Artwork parameters for tea towels: 43cm width X 75cm length. The target market is 25 - 40yr old women.

The text should take up most of the available space on the towel.

There is the opportunity for ongoing work for the right designer.

Thank you for your time.

Target Market(s)

Women aged 25 - 40 who live in Sydney.

Industry/Entity Type

Graphic Design

Requirements
Nice to have
• The feel of the following website:
http://www.plumforkglow.com/

```html
<!DOCTYPE html>
<html lang="en">
<head>
<meta charset="utf-8">
<title>Tea Towel Designs</title>
<link rel="stylesheet" href="https://fonts.googleapis.com/css2?family=Lilita+One&family=Yellowtail&family=Questrial&family=Federo&display=swap">
<style>
  :root {
    --bg: #ffffff;
    --red-deep: #8e0c14;
    --red-mid: #c0141f;
    --red-bright: #e3212b;
    --white: #ffffff;
    --ink: #111111;
    --sea: #2f6fb8;
    --sky: #bfe3f3;
    --sand: #f2c45a;
    --butter: #fbe98a;
    --butter-light: #fff6c4;
    --brown: #6e4216;
  }
  * { margin: 0; padding: 0; box-sizing: border-box; }
  html, body { width: 1200px; height: 1200px; overflow: hidden; background: var(--bg); }
  .canvas { position: relative; width: 1200px; height: 1200px; }

  /* Spaghetti towel */
  .towel-spaghetti {
    position: absolute; left: 48px; top: 26px; width: 408px; height: 712px;
    background: radial-gradient(ellipse at 50% 45%, var(--red-bright), var(--red-mid) 45%, var(--red-deep));
    overflow: hidden;
  }
  .towel-spaghetti .stitch {
    position: absolute; inset: 10px; border: 2px dashed var(--white);
  }
  .towel-spaghetti .swirl {
    position: absolute; border-radius: 40%;
    background: linear-gradient(90deg, rgba(255,220,200,0.05), rgba(255,220,200,0.35), rgba(255,220,200,0.05));
  }
  .swirl-left { left: 22px; top: 130px; width: 110px; height: 290px; }
  .swirl-right { left: 268px; top: 315px; width: 110px; height: 300px; }
  .towel-spaghetti .globe {
    position: absolute; left: -50px; top: 595px; width: 230px; height: 230px; border-radius: 50%;
    background: radial-gradient(circle at 60% 40%, rgba(255,255,255,0.45), rgba(255,255,255,0.12));
  }
  .quote {
    position: absolute; left: 0; right: 0; top: 66px;
    display: flex; flex-direction: column; align-items: center;
    font-family: "Lilita One", sans-serif; font-size: 68px; line-height: 80px;
    color: var(--white); letter-spacing: 1px; text-transform: uppercase;
  }
  .quote-author {
    position: absolute; right: 14px; bottom: 28px;
    font-family: "Yellowtail", cursive; font-size: 26px; color: var(--white);
    transform: rotate(-12deg);
  }

  /* Beaches towel */
  .towel-beaches {
    position: absolute; left: 746px; top: 26px; width: 406px; height: 710px;
    border: 3px solid var(--ink); border-radius: 16px; overflow: hidden; background: var(--white);
    display: flex; flex-direction: column;
  }
  .beach-scene {
    background: linear-gradient(180deg, var(--sky) 0%, var(--sea) 45%, var(--sand) 75%, #f7dc95 100%);
  }
  .beach-name {
    display: flex; align-items: center; justify-content: center;
    font-family: "Questrial", sans-serif; color: var(--ink);
    font-size: 56px; letter-spacing: 0.22em; padding-left: 0.22em; line-height: 1;
    background: var(--white);
  }
  .beach-name.long { letter-spacing: 0.12em; padding-left: 0.12em; }
  .beach-name.tight { letter-spacing: 0.04em; padding-left: 0.04em; font-size: 54px; }

  /* Housewife towel */
  .towel-housewife {
    position: absolute; left: 266px; top: 754px; width: 712px; height: 410px; overflow: hidden;
    background: linear-gradient(135deg, var(--butter-light), var(--butter) 60%, #f6dc6c);
  }
  .frame-line { position: absolute; background: var(--brown); }
  .frame-top-1 { left: 0; right: 0; top: 6px; height: 4px; }
  .frame-top-2 { left: 0; right: 0; top: 14px; height: 2px; }
  .frame-left-1 { top: 0; bottom: 0; left: 6px; width: 4px; }
  .frame-left-2 { top: 0; bottom: 0; left: 14px; width: 2px; }
  .housewife-title {
    position: absolute; left: 34px; right: 10px; top: 18px;
    font-family: "Federo", serif; color: var(--brown);
    font-size: 104px; line-height: 108px; letter-spacing: 1px;
  }
  .kitchen-doodles {
    position: absolute; left: 20px; right: 0; top: 225px; bottom: 0;
    background: linear-gradient(170deg, rgba(110,66,22,0) 10%, rgba(110,66,22,0.22) 40%, rgba(240,150,60,0.25) 70%, rgba(110,66,22,0.08));
    border-radius: 40% 0 0 0;
  }
</style>
</head>
<body>
<div class="canvas">

  <section class="towel-spaghetti">
    <div class="swirl swirl-left" role="img" aria-label="Flowing spaghetti strand illustration"></div>
    <div class="swirl swirl-right" role="img" aria-label="Flowing spaghetti strand illustration"></div>
    <div class="globe" role="img" aria-label="Mesh globe ornament"></div>
    <div class="stitch"></div>
    <div class="quote">
      <span>Everything</span>
      <span>I</span>
      <span>Am,</span>
      <span>I</span>
      <span>Owe</span>
      <span>To</span>
      <span>Spaghetti</span>
    </div>
    <div class="quote-author">Marta Velucci</div>
  </section>

  <section class="towel-beaches">
    <div class="beach-scene" style="height:82px" role="img" aria-label="Beach with palm trees illustration"></div>
    <div class="beach-name" style="height:52px">BONDI</div>
    <div class="beach-scene" style="height:78px" role="img" aria-label="Beach umbrella and sailboat illustration"></div>
    <div class="beach-name long" style="height:60px">COOGEE</div>
    <div class="beach-scene" style="height:82px" role="img" aria-label="Sunset wave and palm illustration"></div>
    <div class="beach-name long" style="height:58px">BRONTE</div>
    <div class="beach-scene" style="height:82px" role="img" aria-label="Shoreline with suitcase and flowers illustration"></div>
    <div class="beach-name long" style="height:58px">CLOVELLY</div>
    <div class="beach-scene" style="height:58px" role="img" aria-label="Beach with ball and crab illustration"></div>
    <div class="beach-name tight" style="flex:1">TAMARAMA</div>
  </section>

  <section class="towel-housewife">
    <div class="frame-line frame-top-1"></div>
    <div class="frame-line frame-top-2"></div>
    <div class="frame-line frame-left-1"></div>
    <div class="frame-line frame-left-2"></div>
    <h1 class="housewife-title">DESPERATE<br>HOUSEWIFE</h1>
    <div class="kitchen-doodles" role="img" aria-label="Music staff with coffee cup, clock, donut, cookies and kitchen items"></div>
  </section>

</div>
</body>
</html>
```